Business Card Design - Commercial Photographer

Professional Photographer requires eye catching creative business card. The design will need to incorporate my current logo in some form & not clash with my website tones & colours ( although website will be re designed in the future ). I'm currently shooting new folios in Commercial, Fashion & Architecture so I'm marketing to professional clients rather than portrait / wedding clients. Looking for something professional & creative.

Industry/Entity Type

Marketing

Requirements
Must have
• Website address - www.brightlenswork.com.au

Phone number - 0471586039

Email - info@brightlenswork.com.au

```html
<!DOCTYPE html>
<html lang="en">
<head>
<meta charset="utf-8">
<title>Bright Lens Work Photography – Business Card</title>
<link rel="stylesheet" href="https://fonts.googleapis.com/css2?family=Saira+Semi+Condensed:wght@500;700&display=swap">
<style>
  :root {
    --stage: #d9d9d7;
    --ink: #0b0b0c;
    --ink-soft: #1c1c1e;
    --paper: #ffffff;
    --paper-shade: #e4e4e4;
    --silver: #b9b9bb;
    --text-light: #f2f2f2;
    --text-dark: #2a2a2c;
  }
  * { box-sizing: border-box; margin: 0; padding: 0; }
  html, body { width: 1200px; height: 871px; overflow: hidden; }
  body {
    background: var(--stage);
    font-family: "Saira Semi Condensed", "Arial Narrow", sans-serif;
    display: flex;
    align-items: center;
    justify-content: center;
    gap: 40px;
  }
  .card {
    position: relative;
    width: 540px;
    height: 309px;
    overflow: hidden;
    box-shadow: 0 14px 30px rgba(0,0,0,0.28);
  }
  .card-front {
    background: linear-gradient(135deg, var(--ink-soft) 0%, var(--ink) 70%);
  }
  .front-glow {
    position: absolute;
    right: 0; top: 0;
    width: 240px; height: 309px;
    background: radial-gradient(ellipse at 60% 30%, rgba(255,255,255,0.07), rgba(255,255,255,0) 70%);
  }
  .brand {
    position: absolute;
    display: flex;
    align-items: center;
    gap: 12px;
  }
  .brand-mark {
    width: 40px; height: 40px;
    background: var(--silver);
  }
  .brand-name {
    font-weight: 700;
    text-transform: uppercase;
    line-height: 1;
    letter-spacing: 1px;
  }
  .card-front .brand { left: 52px; top: 128px; }
  .card-front .brand-name { color: var(--silver); font-size: 26px; }

  .card-back { background: var(--paper); }
  .back-wave { position: absolute; inset: 0; }
  .card-back .brand { left: 46px; top: 42px; }
  .card-back .brand-mark { width: 32px; height: 32px; }
  .card-back .brand-name { color: var(--text-dark); font-size: 21px; }
  .holder-name {
    position: absolute;
    left: 40px; top: 196px;
    color: var(--text-light);
    font-weight: 700;
    font-size: 20px;
    letter-spacing: 1px;
    text-transform: uppercase;
  }
  .contacts {
    position: absolute;
    left: 236px; top: 196px;
    list-style: none;
    color: var(--text-light);
    font-weight: 500;
    font-size: 16px;
  }
  .contacts li {
    display: flex;
    align-items: center;
    gap: 16px;
    height: 28px;
  }
  .contacts svg { width: 16px; height: 16px; flex: none; }
</style>
</head>
<body>

<section class="card card-front" aria-label="Card front">
  <div class="front-glow" role="img" aria-label="Soft dark aperture-style decoration"></div>
  <div class="brand">
    <span class="brand-mark"></span>
    <span class="brand-name">Bright Lens Work Photography</span>
  </div>
</section>

<section class="card card-back" aria-label="Card back">
  <svg class="back-wave" viewBox="0 0 540 309" preserveAspectRatio="none" aria-hidden="true">
    <defs>
      <linearGradient id="paperShade" x1="0" y1="0" x2="1" y2="0">
        <stop offset="0" stop-color="var(--paper-shade)"/>
        <stop offset="0.5" stop-color="var(--paper)"/>
      </linearGradient>
    </defs>
    <rect width="540" height="309" fill="url(#paperShade)"/>
    <path d="M0,128 C110,92 200,132 280,172 S440,238 540,200 L540,309 L0,309 Z" fill="var(--ink)"/>
  </svg>

  <div class="brand">
    <span class="brand-mark"></span>
    <span class="brand-name">Bright Lens Work Photography</span>
  </div>

  <p class="holder-name">Alex Marlow</p>

  <ul class="contacts">
    <li>
      <svg viewBox="0 0 16 16" aria-hidden="true"><path d="M3 2h3l1.5 3.5-2 1.2a9 9 0 0 0 3.8 3.8l1.2-2L14 10v3a1 1 0 0 1-1 1A11 11 0 0 1 2 3a1 1 0 0 1 1-1z" fill="none" stroke="var(--text-light)" stroke-width="1.3"/></svg>
      <span>0471586039</span>
    </li>
    <li>
      <svg viewBox="0 0 16 16" aria-hidden="true"><rect x="1.5" y="3.5" width="13" height="9" fill="none" stroke="var(--text-light)" stroke-width="1.3"/><path d="M1.5 3.5 8 9l6.5-5.5" fill="none" stroke="var(--text-light)" stroke-width="1.3"/></svg>
      <span>info@brightlenswork.com.au</span>
    </li>
    <li>
      <svg viewBox="0 0 16 16" aria-hidden="true"><circle cx="8" cy="8" r="6.3" fill="none" stroke="var(--text-light)" stroke-width="1.3"/><path d="M1.7 8h12.6M8 1.7c-3 3.5-3 9.1 0 12.6M8 1.7c3 3.5 3 9.1 0 12.6" fill="none" stroke="var(--text-light)" stroke-width="1.1"/></svg>
      <span>www.brightlenswork.com.au</span>
    </li>
  </ul>
</section>

</body>
</html>
```